Corvell Executive Search - New Business Card Design Project

We are an executive search firm called Corvell Executive Search based in the UK. We require a custom design for a business card. We're looking to convey a professional service to executives for executive search recruitment services. In terms of colours, we like dark blues and grays (maybe even silver incorporated somewhere if we go for a foiled type of card) but we're open to your artistic flare. See our current logo in attachments. We are totally open on design so long as the design is slick and professional.
Updates

Thanks for all your contributions of various designs. I have to say the quality of work has been amazing which is going to make our job quite difficult in the coming days on making a decision. Thanks to you all that have taken the time to submit designs thus far. We'll keep on reviewing and try to narrow down our selection as soon as possible.

Target Market(s)

Executive Search

Industry/Entity Type

Recruitment

Contact Information for Business Card

Corvell Executive Search,
Exclusively Sourcing & Hiring Senior Leaders
Dominic Haverley, Managing Director,
07742 318906
0117 468 2917
dominic@corvellexecutive.example
corvellexecutive.example
47 Linden Court, Marsh Lane, Bristol, BS9 7QT

Font styles to use
Sans Serif
Other font styles liked:
• Roboto (which is used in our logo)

Requirements
Must have
• Our logo (It has a subtle fade on it from #02071d at top to #333649 at bottom)
• The logo can be on one side or both sides
• Must be elegant and professional
• We have 2nd slogan CONSULT | INSPIRE | INNOVATE | DELIVER which can be incorporated into the card
Nice to have
• Use of blues and grey colours
• Compatible with similar styling to our website corvellexecutive.example
Should not have
• Must not be overly brash
• Must not contain cartoon characters

```html
<!DOCTYPE html>
<html lang="en">
<head>
<meta charset="utf-8">
<title>Corvell Executive Search – Business Card</title>
<link href="https://fonts.googleapis.com/css2?family=Roboto:wght@400;500;700&display=swap" rel="stylesheet">
<style>
  :root {
    --backdrop: #2b2624;
    --silver-light: #f4f4f4;
    --silver-mid: #c9c9c9;
    --silver-dark: #9a9a9a;
    --ink: #111111;
    --card-black: #15161a;
    --card-black-edge: #1d1e23;
    --foil: #cfcfd2;
    --slogan: #6d6e74;
  }
  * { box-sizing: border-box; margin: 0; padding: 0; }
  html, body {
    width: 1200px;
    height: 769px;
    overflow: hidden;
    background: var(--backdrop);
    font-family: "Roboto", Arial, sans-serif;
  }
  .canvas {
    position: relative;
    width: 1200px;
    height: 769px;
  }
  .card {
    position: absolute;
    top: 216px;
    width: 520px;
    height: 336px;
    border-radius: 4px;
    box-shadow: 0 18px 40px rgba(0,0,0,0.45);
  }
  .card--contact {
    left: 60px;
    background: linear-gradient(160deg, var(--silver-dark) 0%, var(--silver-light) 35%, var(--silver-mid) 60%, var(--silver-light) 80%, var(--silver-dark) 100%);
    color: var(--ink);
    display: flex;
    flex-direction: column;
    align-items: center;
    justify-content: center;
    text-align: center;
  }
  .contact__name {
    font-weight: 700;
    font-size: 17px;
    letter-spacing: 0.5px;
  }
  .contact__role {
    font-weight: 500;
    font-size: 12px;
    letter-spacing: 0.6px;
    margin-top: 3px;
  }
  .contact__details {
    margin-top: 26px;
    font-size: 12px;
    line-height: 1.55;
    font-weight: 400;
  }
  .contact__details b { font-weight: 700; }
  .card--brand {
    left: 620px;
    background: linear-gradient(180deg, var(--card-black-edge), var(--card-black));
    display: flex;
    flex-direction: column;
    align-items: center;
    justify-content: center;
  }
  .brand {
    display: flex;
    align-items: center;
    gap: 12px;
  }
  .brand__mark {
    width: 14px;
    height: 14px;
    background: var(--foil);
  }
  .brand__name {
    color: var(--foil);
    font-weight: 500;
    font-size: 24px;
    letter-spacing: 1px;
    text-transform: uppercase;
  }
  .brand__slogan {
    margin-top: 38px;
    color: var(--slogan);
    font-size: 11px;
    font-weight: 400;
    letter-spacing: 2.2px;
  }
</style>
</head>
<body>
<main class="canvas">
  <section class="card card--contact">
    <h1 class="contact__name">DOMINIC HAVERLEY</h1>
    <p class="contact__role">MANAGING DIRECTOR</p>
    <p class="contact__details">
      47 Linden Court, Marsh Lane, Bristol, BS9 7QT<br>
      <b>P:</b> 07742 318906 <b>M:</b> 0117 468 2917 <b>E:</b> dominic@corvellexecutive.example<br>
      <b>W:</b> corvellexecutive.example
    </p>
  </section>

  <section class="card card--brand">
    <div class="brand">
      <span class="brand__mark" aria-hidden="true"></span>
      <h2 class="brand__name">Corvell Executive Search</h2>
    </div>
    <p class="brand__slogan">CONSULT | INSPIRE | INNOVATE | DELIVER</p>
  </section>
</main>
</body>
</html>
```